Vessel Relay - Corporate Stationery (Medical Start Up)
Business Card | Name Tag | Letter Head | Email Signature
Vessel Relay - Corporate Stationery (Medical Start Up) - Medical
Creative Brief
Use specific fonts
Times New Roman and Roboto Regular
Professional
Martin Keogh
CEO
PO BOX R482 Sydney NSW 2000 AUSTRALIA
Martin@vesselrelay.example
www.vesselrelay.example
Powered by Lunar Heron (ABN 98 765 432 101)
(1) Please use the uploaded corporate logo (2) Entries should include one draft that includes the colours of the uploaded logo (3) In addition, Designers are encouraged to present the same logo in different colours (4) The use of a water mark or shadow as a design concept is encouraged (5) Designs need to include example of how the logo will look across the following applications: Business Card | Name Tag | Letter Head | Email Signature (6) The words "Chain of Custody" can be included outside the logo should this be considered desirable by the designer (7) Likewise, elements such as "Vessel Relay", the "shield logo" or concepts there of can be used at the designers discretion (8) Powered by Lunar Heron (ABN 98 765 432 101) needs to be included (9) Use of both sides of the business card is mandatory (10) Please note it's not "Cell", but "Mobile" or "M" or "m" (11) Please use the designated fonts contained in the uploaded file
Design elements on the front and back of the business card are at the designers discretion. A double sided Business Card is preferred.
Dorian Dorian
Dear Designers, Thank you for the innovative designs. A new set of master AI files have been uploaded. Please note that there are different colour versions. Could you please present the stationery in those colours versions plus another other combinations you feel might look good. A separate supplementary design brief has also been uploaded for your assistance. Please read this supplementary design brief. Questions are always welcome.

```html
<!DOCTYPE html>
<html lang="en">
<head>
<meta charset="utf-8">
<title>Vessel Relay – Email Signature</title>
<link href="https://fonts.googleapis.com/css2?family=Roboto:wght@400;500&family=Tinos:wght@400;700&display=swap" rel="stylesheet">
<style>
  :root {
    --stage: #8e8e8e;
    --band: #151515;
    --white: #ffffff;
    --gold: #c9a552;
    --text-light: #e6e6e6;
    --divider: #8a8a8a;
  }
  * { box-sizing: border-box; margin: 0; padding: 0; }
  html, body { width: 1200px; height: 600px; overflow: hidden; }
  body {
    background: var(--stage);
    font-family: "Roboto", Arial, sans-serif;
    position: relative;
  }
  .signature {
    position: absolute;
    left: 41px;
    width: 1126px;
    height: 126px;
    background: var(--band);
    box-shadow: 0 3px 8px rgba(0,0,0,0.25);
  }
  .signature--primary { top: 106px; }
  .signature--shield { top: 305px; }

  .brand-panel {
    position: absolute;
    left: 0; top: 0;
    width: 80px; height: 100%;
    background: var(--white);
    display: flex;
    flex-direction: column;
    justify-content: center;
    align-items: center;
    gap: 4px;
  }
  .brand-panel__name {
    font-family: "Tinos", "Times New Roman", serif;
    font-weight: 700;
    color: var(--gold);
    font-size: 17px;
    line-height: 1.05;
    text-align: center;
  }

  .identity {
    position: absolute;
    left: 202px; top: 36px;
  }
  .identity__name {
    font-family: "Tinos", "Times New Roman", serif;
    font-weight: 700;
    color: var(--text-light);
    font-size: 27px;
    line-height: 1;
  }
  .identity__role {
    color: var(--gold);
    font-size: 17px;
    margin-top: 5px;
  }

  .divider {
    position: absolute;
    top: 30px;
    width: 1px;
    height: 68px;
    background: var(--divider);
  }
  .divider--first { left: 420px; }
  .divider--second { left: 672px; }

  .postal {
    position: absolute;
    left: 451px; top: 37px;
    color: var(--text-light);
    font-size: 16.5px;
    line-height: 23px;
  }

  .contacts {
    position: absolute;
    left: 702px; top: 34px;
    list-style: none;
    color: var(--text-light);
    font-size: 16px;
    line-height: 23px;
  }
  .contacts li { display: flex; align-items: center; gap: 9px; }
  .contacts svg { width: 13px; height: 13px; fill: var(--gold); flex: none; }

  .brand-mark {
    position: absolute;
    left: 985px; top: 16px;
    width: 120px;
    display: flex;
    flex-direction: column;
    align-items: center;
    gap: 8px;
  }
  .brand-mark__dot {
    width: 56px; height: 56px;
    border-radius: 50%;
    background: var(--gold);
  }
  .brand-mark__name {
    font-family: "Tinos", "Times New Roman", serif;
    font-weight: 700;
    color: var(--gold);
    font-size: 16px;
  }
</style>
</head>
<body>

  <section class="signature signature--primary">
    <div class="brand-panel">
      <span class="brand-panel__name">Vessel<br>Relay</span>
    </div>
    <div class="identity">
      <p class="identity__name">Martin Keogh</p>
      <p class="identity__role">CEO</p>
    </div>
    <span class="divider divider--first"></span>
    <p class="postal">PO Box R482<br>Sydney NSW 2000, Australia<br>Powered by Lunar Heron<br>ABN 98 765 432 101</p>
    <span class="divider divider--second"></span>
    <ul class="contacts">
      <li><svg viewBox="0 0 16 16"><path d="M3.6 1.2l2.3 2.6-1.2 1.9c.9 2 2.5 3.7 4.6 4.6l1.9-1.2 2.6 2.3-1.4 2.7C7.4 13.9 2.1 8.6 1 3.6z"/></svg>+61 2 5550 1842</li>
      <li><svg viewBox="0 0 16 16"><path d="M4.5 1h7v14h-7zM5.7 2.6v9.6h4.6V2.6zM7.3 13h1.4v1H7.3z"/></svg>+61 0 455 019 273</li>
      <li><svg viewBox="0 0 16 16"><path d="M1 3.5h14v9H1zM2.4 4.6 8 9l5.6-4.4z"/></svg>martin@vesselrelay.example</li>
      <li><svg viewBox="0 0 16 16"><circle cx="8" cy="8" r="7"/></svg>www.vesselrelay.example</li>
    </ul>
  </section>

  <section class="signature signature--shield">
    <div class="brand-panel">
      <span class="brand-panel__name">Vessel<br>Relay</span>
    </div>
    <div class="identity">
      <p class="identity__name">Martin Keogh</p>
      <p class="identity__role">CEO</p>
    </div>
    <span class="divider divider--first"></span>
    <p class="postal">PO Box R482<br>Sydney NSW 2000, Australia<br>Powered by Lunar Heron<br>ABN 98 765 432 101</p>
    <span class="divider divider--second"></span>
    <ul class="contacts">
      <li><svg viewBox="0 0 16 16"><path d="M3.6 1.2l2.3 2.6-1.2 1.9c.9 2 2.5 3.7 4.6 4.6l1.9-1.2 2.6 2.3-1.4 2.7C7.4 13.9 2.1 8.6 1 3.6z"/></svg>+61 2 5550 1842</li>
      <li><svg viewBox="0 0 16 16"><path d="M4.5 1h7v14h-7zM5.7 2.6v9.6h4.6V2.6zM7.3 13h1.4v1H7.3z"/></svg>+61 0 455 019 273</li>
      <li><svg viewBox="0 0 16 16"><path d="M1 3.5h14v9H1zM2.4 4.6 8 9l5.6-4.4z"/></svg>martin@vesselrelay.example</li>
      <li><svg viewBox="0 0 16 16"><circle cx="8" cy="8" r="7"/></svg>www.vesselrelay.example</li>
    </ul>
    <div class="brand-mark">
      <span class="brand-mark__dot"></span>
      <span class="brand-mark__name">Vessel Relay</span>
    </div>
  </section>

</body>
</html>
```